Building Certification Company needs a professional letterhead and report template

We are a modern company within an ageing industry. Our industry is responsible for life safety aspects of the built environment, we ensure buildings are safe and fit for occupation.

We use letterhead and reports everyday, we need a smart and professional letterhead that reflects the serious nature of the work we do. We also require a report template of the same ilk.

Target Market(s)

Our target market will consist mainly of professional architects, developers and construction companies.

Industry/Entity Type

Industry

Requirements
Must have
• The letterhead must have:-
Our logo
Our company details, including address, website, email, phone

Address - Suite 208 / 45 Harwick Lane Dunmore NSW 2100

Website - www.quillstonecompliance.example.au

Email - info@qsc.example.au

Phone - 02 5550 3846

The report template must have:-
A title page, which is to incorporate our logo or an aspect of our logo, get creative people.

```html
<!DOCTYPE html>
<html lang="en">
<head>
<meta charset="utf-8">
<title>Quillstone Compliance – Letterhead</title>
<link rel="stylesheet" href="https://fonts.googleapis.com/css2?family=Source+Sans+3:wght@400;600&display=swap">
<style>
  :root {
    --brand-blue: #4169c8;
    --brand-slate: #4f6977;
    --ink: #3a3a3a;
    --paper: #ffffff;
  }
  html, body {
    margin: 0;
    padding: 0;
    overflow: hidden;
    background: var(--paper);
  }
  .letterhead {
    position: relative;
    width: 848px;
    height: 1200px;
    overflow: hidden;
    background: var(--paper);
    font-family: "Source Sans 3", Arial, sans-serif;
  }
  .brand {
    position: absolute;
    left: 34px;
    top: 40px;
    display: flex;
    align-items: center;
    gap: 16px;
  }
  .brand-mark {
    width: 64px;
    height: 64px;
    background: var(--brand-slate);
  }
  .brand-name {
    margin: 0;
    font-size: 30px;
    font-weight: 600;
    line-height: 1.05;
    letter-spacing: 3px;
    text-transform: uppercase;
    color: var(--brand-blue);
  }
  .contact {
    position: absolute;
    left: 536px;
    top: 45px;
    margin: 0;
    padding: 0;
    list-style: none;
    font-size: 11.5px;
    line-height: 16px;
    color: var(--ink);
  }
  .contact li {
    display: flex;
    align-items: center;
    gap: 8px;
    white-space: nowrap;
  }
  .contact-icon {
    width: 10px;
    height: 10px;
    flex: none;
    fill: none;
    stroke: var(--brand-blue);
    stroke-width: 1.4;
  }
  .header-rule {
    position: absolute;
    left: 0;
    width: 848px;
  }
  .header-rule--blue {
    top: 150px;
    height: 6px;
    background: var(--brand-blue);
  }
  .header-rule--slate {
    top: 162px;
    height: 3px;
    background: var(--brand-slate);
  }
</style>
</head>
<body>
<main class="letterhead">
  <header class="brand">
    <div class="brand-mark"></div>
    <p class="brand-name">Quillstone<br>Compliance</p>
  </header>

  <ul class="contact">
    <li>
      <svg class="contact-icon" viewBox="0 0 10 10"><path d="M5 9.5 C2 6 2 4.5 2 3.8 A3 3 0 0 1 8 3.8 C8 4.5 8 6 5 9.5 Z"/><circle cx="5" cy="3.8" r="1"/></svg>
      Suite 208 / 45 Harwick Lane, Dunmore. NSW-2100
    </li>
    <li>
      <svg class="contact-icon" viewBox="0 0 10 10"><rect x="2.8" y="0.8" width="4.4" height="8.4" rx="0.8"/></svg>
      02 5550 3846
    </li>
    <li>
      <svg class="contact-icon" viewBox="0 0 10 10"><rect x="0.8" y="2" width="8.4" height="6" rx="0.5"/><path d="M0.8 2.3 L5 5.5 L9.2 2.3"/></svg>
      info@qsc.example.au
    </li>
    <li>
      <svg class="contact-icon" viewBox="0 0 10 10"><circle cx="5" cy="5" r="4"/><path d="M1 5 H9 M5 1 C3 3.5 3 6.5 5 9 M5 1 C7 3.5 7 6.5 5 9"/></svg>
      www.quillstonecompliance.example.au
    </li>
  </ul>

  <div class="header-rule header-rule--blue"></div>
  <div class="header-rule header-rule--slate"></div>
</main>
</body>
</html>
```